Jewelry Back Card Graphic Design

I am looking for a graphic design to print out and put in the back of the jewelry box for my long-distance jewelry. I attached an example that I am now using for the "still harbor jewelry" so you can see what it's used for.

But this card needs to relate to people who are in a long-distance relationship or friendship, so it needs to resonate with them when they see it on the website and open the box if they receive the jewelry as a gift.

I attached a rough idea that I sketched myself, but you can be creative and create anything else if you have a better idea.

It needs to be square.

Looking forward to the results!

```html
<!DOCTYPE html>
<html lang="en">
<head>
<meta charset="utf-8">
<title>A True Connection – Back Card</title>
<link rel="stylesheet" href="https://fonts.googleapis.com/css2?family=Barlow:wght@400;600&display=swap">
<style>
  :root {
    --sky-pink: #ecbccb;
    --sky-peach: #eac39c;
    --sky-gold: #e9bf76;
    --sun-amber: #ef8a3c;
    --hill-mauve: #a98a9c;
    --meadow-green: #7f8a4a;
    --text-bronze: #a87b4f;
    --brand-white: #ffffff;
  }

  html, body {
    margin: 0;
    padding: 0;
    width: 1200px;
    height: 1200px;
    overflow: hidden;
  }

  .card {
    position: relative;
    width: 1200px;
    height: 1200px;
    overflow: hidden;
    font-family: "Barlow", "Helvetica Neue", Arial, sans-serif;
  }

  .scene {
    position: absolute;
    inset: 0;
    background: linear-gradient(180deg,
      var(--sky-pink) 0%,
      var(--sky-pink) 32%,
      var(--sky-peach) 50%,
      var(--sky-gold) 62%,
      var(--sun-amber) 74%,
      var(--hill-mauve) 86%,
      var(--meadow-green) 100%);
  }

  .tagline {
    position: absolute;
    top: 217px;
    left: 0;
    width: 100%;
    margin: 0;
    text-align: center;
    color: var(--text-bronze);
    font-weight: 400;
    font-size: 115px;
    line-height: 135px;
    letter-spacing: -0.5px;
  }

  .tagline strong {
    font-weight: 600;
  }

  .brand-name {
    position: absolute;
    left: 0;
    width: 100%;
    top: 1008px;
    margin: 0;
    text-align: center;
    color: var(--brand-white);
    font-weight: 600;
    font-size: 56px;
    line-height: 56px;
    letter-spacing: 10px;
    text-transform: uppercase;
  }
</style>
</head>
<body>
  <main class="card">
    <div class="scene" role="img" aria-label="Illustrated sunset over rolling purple hills and a green meadow, with a lone silhouetted tree on the right"></div>

    <h1 class="tagline">a true <strong>connection</strong><br>goes beyond horizons</h1>

    <p class="brand-name">Far<br>Shores</p>
  </main>
</body>
</html>
```